Unique business card design

We are looking for a design that reflects our unique social media and online marketing agency "Kestrel Media". We are a young agency with a focus on speakers, coaches and trainers. In other words, we support people who want to do good with their work and help other people live a happier, more successful and fulfilling life, reach as many people as possible with their work and thus have an influence. Our values are: sustainability, creating added value, individuality, proactivity. We want our clients to feel comfortable with us and that's why the relationship with them is very important to us. We want every customer to become a lifelong friend of the company. Most of our clients are premium coaches, meaning they are in the higher priced segment and expect seriousness, professionalism and quality. All of these things should reflect our business card as well. I look forward to feedback. Best regards, Tomas Wylander

```html
<!DOCTYPE html>
<html lang="en">
<head>
<meta charset="utf-8">
<title>Kestrel Media – Business Card</title>
<link rel="stylesheet" href="https://fonts.googleapis.com/css2?family=Saira:wght@400;600;700&display=swap">
<style>
  :root {
    --backdrop: #e7e4df;
    --navy-deep: #02023f;
    --navy: #0d0d4d;
    --violet: #4a4aa0;
    --brand-blue: #1f5fbf;
    --ink-grey: #4f4f55;
    --paper: #f4f4f4;
    --rule: #cfcfcf;
    --dot-grey: #8a8a93;
  }
  * { box-sizing: border-box; margin: 0; padding: 0; }
  html, body {
    width: 1200px; height: 960px; overflow: hidden;
    background: var(--backdrop);
    font-family: "Saira", sans-serif;
  }
  .canvas { position: relative; width: 1200px; height: 960px; }

  .card {
    position: absolute; left: 320px; width: 600px; height: 342px;
    box-shadow: 0 3px 8px rgba(0,0,0,.25);
  }

  /* Back side */
  .card-back { top: 108px; background: var(--navy-deep); }
  .card-back .brand {
    position: absolute; left: 0; right: 0; top: 118px;
    display: flex; flex-direction: column; align-items: center;
  }
  .brand-row { display: flex; align-items: center; gap: 14px; }
  .brand-square { width: 40px; height: 40px; background: var(--brand-blue); }
  .card-back .brand-name { color: #ffffff; font-size: 38px; font-weight: 400; letter-spacing: .5px; line-height: 1; }
  .card-back .tagline { color: var(--violet); font-size: 15px; margin-top: 10px; letter-spacing: .5px; }
  .social-row {
    position: absolute; top: 276px; left: 0; right: 0;
    display: flex; justify-content: center; gap: 3px;
  }
  .social-dot { width: 26px; height: 26px; border-radius: 50%; background: var(--dot-grey); }

  /* Front side */
  .card-front { top: 493px; background: var(--paper); }
  .contact-block {
    position: absolute; right: 346px; top: 64px; text-align: right;
  }
  .person-name { color: var(--navy); font-size: 21px; font-weight: 700; line-height: 1; }
  .person-role { color: var(--violet); font-size: 14px; font-weight: 700; letter-spacing: .5px; margin-top: 4px; }
  .address { color: var(--ink-grey); font-size: 15px; line-height: 20px; margin-top: 16px; }
  .contact-list { list-style: none; margin-top: 10px; }
  .contact-list li {
    color: var(--ink-grey); font-size: 15px; line-height: 20px;
    display: flex; justify-content: flex-end; align-items: center; gap: 10px;
  }
  .contact-list svg { width: 14px; height: 14px; fill: var(--navy); flex: none; margin-right: -18px; }
  .contact-list li { padding-right: 0; }
  .contact-list { margin-right: -26px; }
  .contact-list li span { margin-right: 26px; }
  .divider {
    position: absolute; left: 280px; top: 66px; width: 1px; height: 210px;
    background: var(--rule);
  }
  .card-front .brand { position: absolute; left: 310px; top: 118px; }
  .card-front .brand-name { color: var(--navy); font-size: 36px; font-weight: 400; line-height: 1; }
  .card-front .tagline { color: var(--brand-blue); font-size: 15px; margin-top: 12px; letter-spacing: .5px; }
</style>
</head>
<body>
<main class="canvas">

  <section class="card card-back" aria-label="Card back">
    <div class="brand">
      <div class="brand-row">
        <div class="brand-square"></div>
        <span class="brand-name">Kestrel Media</span>
      </div>
      <p class="tagline">Online Marketing Services</p>
    </div>
    <div class="social-row" aria-label="Social media links">
      <span class="social-dot"></span><span class="social-dot"></span><span class="social-dot"></span><span class="social-dot"></span><span class="social-dot"></span>
    </div>
  </section>

  <section class="card card-front" aria-label="Card front">
    <div class="contact-block">
      <h1 class="person-name">TOMAS WYLANDER</h1>
      <p class="person-role">PRESIDENT</p>
      <p class="address">2716 Alder Crest Road<br>Brookvale, NY 11482</p>
      <ul class="contact-list">
        <li><span>555 0148 2209</span><svg viewBox="0 0 16 16"><path d="M2 5c2-3 10-3 12 0v2h-3V5.5H5V7H2zM3 8h10l1 6H2z"/></svg></li>
        <li><span>555 0172 6631</span><svg viewBox="0 0 16 16"><path d="M4 0h8v16H4zM5.5 2v10h5V2z"/></svg></li>
        <li><span>555 0193 4470</span><svg viewBox="0 0 16 16"><path d="M4 1h8v4H4zM1 6h14v7h-3v-2H4v2H1zM5 12h6v3H5z"/></svg></li>
        <li><span>tomas@kestrel.com</span><svg viewBox="0 0 16 16"><path d="M1 3h14v2L8 9 1 5zM1 7l7 4 7-4v6H1z"/></svg></li>
        <li><span>www.kestrel.com</span><svg viewBox="0 0 16 16"><circle cx="8" cy="8" r="7"/></svg></li>
      </ul>
    </div>
    <div class="divider"></div>
    <div class="brand">
      <div class="brand-row">
        <div class="brand-square"></div>
        <span class="brand-name">Kestrel Media</span>
      </div>
      <p class="tagline">Online Marketing Services</p>
    </div>
  </section>

</main>
</body>
</html>
```